Booth52 - Tablet App Design Project

I have a Tablet app that serves as a restaurant reservation system. The design that i currently have is very basic pearl design. I am looking for it to have a much more professional appeal.

Please review the attached document which contains all of the screen shots for the app.

This Project has now been Guaranteed.  I look forward to reviewing your designs.

Glen

Reason: I am extending my deadline because i just changed this contest to guaranteed and have received a ton more "acceptances" because of it and I want to give those designers a chance to submit a design.

Target Market(s)

restaurant owners

Industry/Entity Type

Restaurant

Requirements
Must have
• On the seating chart i am changing the feature that shows the tables highlighted and instead would like that replace with a badge. So the list of wait staff across the top of the seating chart would instead have a number next to their name and would correspond with the badge on the table to determine their section.

So for example:
Ana would have a number 1 in front of her name and tables 18, 19, 20, and 31 would have a little badge in the upper right hand corner with the number "1" inside the badge.
Tess would have a number 2 in front of her name and tables 6, 7, and 11 would have a little badge in the upper right hand corner with the number " 2" inside the badge.
Rita would have a number 3 in front of her name and tables 12, 13, 27, 28, 29, and 30 would have a little badge in the upper right hand corner with the number " 3" inside the badge.

The names on the top will all be ONE color

Also, i would like an icon developed to replace the "C" you see next to some of the people's name in the reservation and waitlist slots. Also, i would like a better looking "check mark".

```html
<!DOCTYPE html>
<html lang="en">
<head>
<meta charset="utf-8">
<title>Booth52 – Seating</title>
<link href="https://fonts.googleapis.com/css2?family=Arimo:ital,wght@0,400;0,700;1,400;1,700&display=swap" rel="stylesheet">
<style>
:root{
  --status:#000;
  --header:#fff;
  --floor:#a9a9a9;
  --floor-dark:#9a9a9a;
  --orange-top:#d9800f;
  --orange-bot:#a9560a;
  --gray-top:#f0f0f0;
  --gray-bot:#c6c6c6;
  --badge:#8d8d8d;
  --blue-top:#3c9ae6;
  --blue-bot:#0f63bd;
  --home-top:#aadaf6;
  --home-bot:#5fb0e3;
  --wait-head:#f6e3a6;
  --wait-row:#fdf6d8;
  --slot-head:#cdd2f5;
  --slot-row:#e4e8f8;
  --full-head:#cfcfcf;
  --full-row:#e6e6e6;
  --ink:#333;
  --muted:#555;
  --accent:#1a6fd1;
  --tan:#8a5a12;
}
*{box-sizing:border-box;margin:0;padding:0}
html,body{width:1200px;height:900px;overflow:hidden;background:#fff}
body{position:relative;font-family:"Arimo",Arial,sans-serif;color:var(--ink)}
.status-bar{position:absolute;left:0;top:0;width:1200px;height:22px;background:var(--status);color:#fff;font-size:14px;font-weight:700;display:flex;align-items:center;justify-content:space-between;padding:0 10px}
.status-bar .time{position:absolute;left:0;right:0;text-align:center}
.app-header{position:absolute;left:0;top:22px;width:1200px;height:40px;background:var(--header)}
.brand{position:absolute;left:12px;top:6px;display:flex;align-items:center;gap:6px;font-size:24px;color:#5aaee0}
.brand-mark{width:22px;height:22px;background:#9fc6df;border-radius:3px}
.nav-btn{position:absolute;top:3px;height:34px;border-radius:6px;background:linear-gradient(var(--blue-top),var(--blue-bot));color:#fff;font-weight:700;font-size:20px;display:flex;align-items:center;justify-content:center;box-shadow:0 2px 2px rgba(0,0,0,.25)}
.nav-btn.home{background:linear-gradient(var(--home-top),var(--home-bot))}
.staff-row{position:absolute;top:62px;left:0;width:1200px;height:33px;background:var(--header);border-bottom:1px solid #ddd}
.staff{position:absolute;top:5px;display:flex;align-items:center;gap:4px;font-size:20px;font-weight:700;color:var(--ink)}
.num{width:22px;height:22px;border-radius:50%;background:var(--badge);color:#fff;font-size:14px;display:flex;align-items:center;justify-content:center;font-weight:700}
.list-panel{position:absolute;left:0;top:95px;width:398px;height:805px;display:flex;flex-direction:column;border-right:1px solid #bbb;background:#fff}
.list-head{display:flex;align-items:center;padding:0 12px;font-size:21px;font-weight:700;border-bottom:1px solid #bbb}
.list-head.wait{height:44px;background:linear-gradient(#fbeec0,var(--wait-head));color:var(--tan);justify-content:space-between}
.list-head.slot{height:45px;background:linear-gradient(#dde0fa,var(--slot-head));color:var(--accent)}
.list-head.full{height:46px;background:linear-gradient(#dcdcdc,var(--full-head));color:var(--muted)}
.list-head .cap{margin-left:72px}
.list-head .plus{margin-left:auto;font-size:26px;font-weight:700}
.entry{position:relative;padding:0 12px;border-bottom:1px solid #c8c8c8;display:flex;flex-direction:column;justify-content:center}
.entry.wait{background:var(--wait-row);height:47px}
.entry.slot{background:var(--slot-row);height:46px}
.entry.full{background:var(--full-row);height:47px}
.entry.noted{height:58px}
.entry .line{display:flex;align-items:center;gap:5px;font-size:20px;font-weight:700;color:var(--ink)}
.entry .note{font-size:12px;font-style:italic;font-weight:700;color:#444;margin-top:3px}
.tag{height:24px;border-radius:4px;display:inline-flex;align-items:center;gap:3px;padding:0 4px;font-size:15px;font-weight:700;color:#fff}
.tag.time{background:linear-gradient(#4aa6ec,#1676cf)}
.tag.party{background:linear-gradient(#9a9a9a,#707070)}
.tag.table{background:linear-gradient(#d9800f,#a9560a)}
.tag svg{width:18px;height:18px}
.alert{width:24px;height:24px;border-radius:50%;background:#1c82dd;color:#fff;font-weight:700;font-size:17px;display:inline-flex;align-items:center;justify-content:center}
.check{position:absolute;right:10px;top:50%;margin-top:-13px;width:26px;height:26px}
.floor{position:absolute;left:399px;top:95px;width:801px;height:805px;background:linear-gradient(var(--floor),var(--floor-dark))}
.tbl{position:absolute;display:flex;align-items:center;justify-content:center;font-size:20px;font-weight:700;color:#5a3306;background:linear-gradient(var(--orange-top),var(--orange-bot));border-radius:5px;box-shadow:0 2px 3px rgba(0,0,0,.3)}
.tbl.gray{background:linear-gradient(var(--gray-top),var(--gray-bot));color:#555}
.tbl.round{border-radius:50%}
.tbl.diamond{transform:rotate(45deg);border-radius:5px}
.tbl.diamond span{transform:rotate(-45deg)}
.tbl.dark{background:linear-gradient(#b86a0c,#8e4a07)}
.seat-badge{position:absolute;width:22px;height:22px;border-radius:50%;background:var(--badge);border:2px solid #fff;color:#fff;font-size:13px;font-weight:700;display:flex;align-items:center;justify-content:center;box-shadow:0 1px 2px rgba(0,0,0,.3)}
</style>
</head>
<body>
<div class="status-bar"><span>Tablet</span><span class="time">4:20 PM</span><span>▮</span></div>

<header class="app-header">
  <div class="brand"><span class="brand-mark"></span><span>Booth52</span></div>
  <div class="nav-btn home" style="left:490px;width:102px">Home</div>
  <div class="nav-btn" style="left:593px;width:178px">Edit Floor Plans</div>
  <div class="nav-btn" style="left:779px;width:191px">Manage Sections</div>
  <div class="nav-btn" style="left:977px;width:213px">Select Floor Plan</div>
</header>

<nav class="staff-row">
  <div class="staff" style="left:11px"><span class="num">1</span>Ana</div>
  <div class="staff" style="left:102px"><span class="num">2</span>Tess</div>
  <div class="staff" style="left:190px"><span class="num">3</span>Rita</div>
  <div class="staff" style="left:285px"><span class="num">4</span>Vev</div>
  <div class="staff" style="left:371px"><span class="num">5</span>Jone</div>
  <div class="staff" style="left:475px"><span class="num">6</span>Kimmy</div>
  <div class="staff" style="left:604px"><span class="num">7</span>Eric</div>
  <div class="staff" style="left:696px"><span class="num">8</span>Mike</div>
  <div class="staff" style="left:803px"><span class="num">9</span>Ana</div>
</nav>

<svg width="0" height="0" style="position:absolute">
  <defs>
    <symbol id="i-clock" viewBox="0 0 18 18"><circle cx="9" cy="9" r="7" fill="none" stroke="#fff" stroke-width="2"/><path d="M9 5v4l3 2" fill="none" stroke="#fff" stroke-width="2" stroke-linecap="round"/></symbol>
    <symbol id="i-person" viewBox="0 0 18 18"><circle cx="9" cy="6" r="4" fill="#fff"/><path d="M2 17c0-4 3-6 7-6s7 2 7 6z" fill="#fff"/></symbol>
    <symbol id="i-check" viewBox="0 0 26 26"><circle cx="13" cy="13" r="12" fill="#1c82dd" stroke="#fff" stroke-width="2"/><path d="M7 13.5l4 4 8-9" fill="none" stroke="#fff" stroke-width="3" stroke-linecap="round" stroke-linejoin="round"/></symbol>
  </defs>
</svg>

<aside class="list-panel">
  <div class="list-head wait">Wait List<span class="plus">+</span></div>
  <div class="entry wait"><div class="line"><span class="tag time"><svg><use href="#i-clock"/></svg>5</span><span class="tag party"><svg><use href="#i-person"/></svg>4</span>Elise Marlow</div></div>
  <div class="entry wait"><div class="line"><span class="tag time"><svg><use href="#i-clock"/></svg>5</span><span class="tag party"><svg><use href="#i-person"/></svg>2</span>Glen Sharp</div></div>
  <div class="entry wait"><div class="line"><span class="tag time"><svg><use href="#i-clock"/></svg>25</span><span class="tag party"><svg><use href="#i-person"/></svg>4</span>Dora Lane</div></div>
  <div class="entry wait"><div class="line"><span class="tag time"><svg><use href="#i-clock"/></svg>25</span><span class="tag party"><svg><use href="#i-person"/></svg>3</span>Abigail Renard</div></div>

  <div class="list-head slot">12:00 PM<span class="cap">Open 9(22)</span><span class="plus">+</span></div>
  <div class="entry slot noted" style="height:59px"><div class="line"><span class="tag party"><svg><use href="#i-person"/></svg>4</span><span class="tag table">T 11</span>Ray Stone</div><div class="note">I would like a booth in the corner</div><svg class="check"><use href="#i-check"/></svg></div>
  <div class="entry slot"><div class="line"><span class="tag party"><svg><use href="#i-person"/></svg>3</span>Ana Voss</div><svg class="check"><use href="#i-check"/></svg></div>
  <div class="entry slot noted" style="height:60px"><div class="line"><span class="alert">!</span><span class="tag party"><svg><use href="#i-person"/></svg>2</span><span class="tag table">T 1</span>Leo Grant</div><div class="note">Patio table if available</div></div>

  <div class="list-head full">12:15 PM<span class="cap">Full</span></div>
  <div class="entry full"><div class="line"><span class="tag party"><svg><use href="#i-person"/></svg>4</span>Fred Barr</div><svg class="check"><use href="#i-check"/></svg></div>
  <div class="entry full noted" style="height:57px"><div class="line"><span class="alert">!</span><span class="tag party"><svg><use href="#i-person"/></svg>5</span><span class="tag table">T 12</span>Owen Darby</div><div class="note">Birthday celebration</div><svg class="check"><use href="#i-check"/></svg></div>
  <div class="entry full noted"><div class="line"><span class="tag party"><svg><use href="#i-person"/></svg>2</span>Mark Foley</div><div class="note">We have one person that needs gluten free food</div><svg class="check"><use href="#i-check"/></svg></div>
  <div class="entry full"><div class="line"><span class="tag party"><svg><use href="#i-person"/></svg>4</span>Sam Holden</div></div>

  <div class="list-head slot" style="height:50px">12:30 PM<span class="cap">Open 12(20)</span><span class="plus">+</span></div>
  <div class="entry slot" style="height:45px"><div class="line"><span class="tag party"><svg><use href="#i-person"/></svg>4</span>Joan Pereira</div><svg class="check"><use href="#i-check"/></svg></div>
</aside>

<main class="floor"></main>

<div class="tbl round" style="left:417px;top:155px;width:90px;height:90px">1</div><div class="seat-badge" style="left:482px;top:157px">9</div>
<div class="tbl round" style="left:417px;top:292px;width:90px;height:90px">2</div><div class="seat-badge" style="left:482px;top:294px">9</div>
<div class="tbl round" style="left:417px;top:430px;width:90px;height:90px">3</div><div class="seat-badge" style="left:482px;top:432px">9</div>
<div class="tbl round gray" style="left:417px;top:567px;width:90px;height:90px">4</div><div class="seat-badge" style="left:482px;top:569px">8</div>
<div class="tbl round" style="left:417px;top:707px;width:90px;height:90px">5</div><div class="seat-badge" style="left:482px;top:709px">8</div>

<div class="tbl" style="left:580px;top:158px;width:86px;height:84px">6</div><div class="seat-badge" style="left:651px;top:148px">2</div>
<div class="tbl" style="left:580px;top:293px;width:86px;height:86px">7</div><div class="seat-badge" style="left:651px;top:283px">2</div>
<div class="tbl" style="left:580px;top:431px;width:86px;height:85px">8</div><div class="seat-badge" style="left:651px;top:421px">7</div>
<div class="tbl" style="left:580px;top:570px;width:86px;height:85px">9</div><div class="seat-badge" style="left:651px;top:560px">7</div>
<div class="tbl gray" style="left:580px;top:706px;width:86px;height:87px">10</div><div class="seat-badge" style="left:651px;top:696px">7</div>

<div class="tbl gray" style="left:715px;top:156px;width:133px;height:86px">11</div><div class="seat-badge" style="left:833px;top:147px">2</div>
<div class="tbl" style="left:902px;top:160px;width:134px;height:85px">12</div><div class="seat-badge" style="left:1021px;top:151px">3</div>
<div class="tbl" style="left:1084px;top:157px;width:88px;height:86px">13</div><div class="seat-badge" style="left:1157px;top:148px">3</div>

<div class="tbl" style="left:740px;top:295px;width:42px;height:132px">18</div><div class="seat-badge" style="left:768px;top:284px">1</div>
<div class="tbl" style="left:832px;top:297px;width:42px;height:132px">19</div><div class="seat-badge" style="left:860px;top:285px">1</div>
<div class="tbl gray" style="left:925px;top:295px;width:42px;height:132px">20</div><div class="seat-badge" style="left:953px;top:284px">1</div>

<div class="tbl gray" style="left:1040px;top:288px;width:41px;height:48px">27</div><div class="seat-badge" style="left:1070px;top:283px">3</div>
<div class="tbl gray" style="left:1108px;top:288px;width:41px;height:48px">29</div><div class="seat-badge" style="left:1138px;top:283px">3</div>
<div class="tbl gray" style="left:1040px;top:363px;width:41px;height:42px">28</div><div class="seat-badge" style="left:1070px;top:355px">3</div>
<div class="tbl gray" style="left:1108px;top:363px;width:41px;height:42px">30</div><div class="seat-badge" style="left:1138px;top:355px">3</div>

<div class="tbl diamond" style="left:741px;top:477px;width:38px;height:38px"><span>22</span></div><div class="seat-badge" style="left:760px;top:461px">4</div>
<div class="tbl diamond gray" style="left:808px;top:477px;width:38px;height:38px"><span>23</span></div><div class="seat-badge" style="left:827px;top:461px">4</div>
<div class="tbl diamond" style="left:741px;top:546px;width:38px;height:38px"><span>24</span></div><div class="seat-badge" style="left:760px;top:531px">4</div>
<div class="tbl diamond" style="left:813px;top:546px;width:38px;height:38px"><span>25</span></div><div class="seat-badge" style="left:834px;top:531px">4</div>

<div class="tbl round gray" style="left:877px;top:473px;width:46px;height:46px">32</div><div class="seat-badge" style="left:903px;top:465px">4</div>
<div class="tbl round gray" style="left:944px;top:473px;width:46px;height:46px">33</div><div class="seat-badge" style="left:970px;top:465px">4</div>
<div class="tbl round gray" style="left:877px;top:543px;width:46px;height:46px">34</div><div class="seat-badge" style="left:903px;top:535px">4</div>
<div class="tbl round gray" style="left:944px;top:543px;width:46px;height:46px">35</div><div class="seat-badge" style="left:970px;top:535px">4</div>

<div class="tbl dark" style="left:1039px;top:458px;width:132px;height:131px">31</div><div class="seat-badge" style="left:1156px;top:450px">1</div>

<div class="tbl" style="left:715px;top:637px;width:138px;height:41px">21</div><div class="seat-badge" style="left:840px;top:626px">5</div>
<div class="tbl gray" style="left:901px;top:639px;width:86px;height:41px">26</div><div class="seat-badge" style="left:979px;top:626px">5</div>
<div class="tbl" style="left:1039px;top:639px;width:132px;height:41px">36</div><div class="seat-badge" style="left:1156px;top:626px">5</div>

<div class="tbl diamond gray" style="left:725px;top:719px;width:66px;height:66px"><span>14</span></div><div class="seat-badge" style="left:758px;top:700px">6</div>
<div class="tbl diamond" style="left:845px;top:719px;width:66px;height:66px"><span>15</span></div><div class="seat-badge" style="left:878px;top:700px">6</div>
<div class="tbl diamond" style="left:960px;top:719px;width:66px;height:66px"><span>16</span></div><div class="seat-badge" style="left:993px;top:700px">6</div>
<div class="tbl diamond" style="left:1071px;top:719px;width:66px;height:66px"><span>17</span></div><div class="seat-badge" style="left:1104px;top:700px">6</div>
</body>
</html>
```